3 Medical Provider Brochures targeted at doctors and patients

We are a diagnostic imaging provider.

We need 3 brochure layouts.

1) A 4-fold with our 4 locations...one on each panel
2) A single-sheet brochure marketing each of our procedures to the referring physicians. (a shell, one completed so we clone the rest)
3) A single-sheet brochure handout containing information about certain exams and ways to prepare for our patients' education. (a shell, one completed so we can clone the rest)

Target Market(s)

4-fold target is for the referral coordinator in a doctors office, so they can find our location at-a-glance
One of the single broadsheets to the referring physician marketing a particular modality (CAT Scan, MRI, X-ray, Ultrasound, Mammography, Breast Biopsy)
The other single Broadsheet is marketed to patients but handed out by doctors who want to send patients to be scanned at our facility.

Industry/Entity Type

Medical Imaging

Font styles to use
Sans Serif

Colors
3276b5
0255a3
85cae6
ffffff

Requirements
Must have
• The 4-fold should be easy to read at-a-glance but contain some branding.
• The doctor-facing broadsheet should be in a the form of a shell, so we can do one for each of our modalities
• The patient-facing should be a shell as well, so we can do one for each of our major exams.
• Our name is KEL MRI and Imaging Centers. KEL means Kind Every Lane. KEL IS Kind Every Lane.
Nice to have
• Friendly faces, but professional and knowledgeable.
• Easy-to-update brochure shell contents

```html
<!DOCTYPE html>
<html lang="en">
<head>
<meta charset="utf-8">
<title>KEL MRI and Imaging Centers – Brochure Set</title>
<link href="https://fonts.googleapis.com/css2?family=Open+Sans:ital,wght@0,400;0,600;0,700;1,400;1,600&family=Roboto+Condensed:wght@700&family=Poppins:wght@300;600;700&display=swap" rel="stylesheet">
<style>
:root{
  --blue:#0255a3;
  --blue-mid:#3276b5;
  --blue-light:#85cae6;
  --white:#ffffff;
  --grey:#8c8c8c;
  --grey-light:#dcdcdc;
  --ink:#222;
  --bg:#e6e6e6;
}
*{box-sizing:border-box;margin:0;padding:0}
html,body{width:1200px;height:1200px;overflow:hidden;background:var(--bg)}
body{position:relative;font-family:"Open Sans",sans-serif;color:var(--ink)}

/* ---------- four-fold ---------- */
.fourfold{position:absolute;left:60px;top:40px;width:1080px;height:490px;background:linear-gradient(160deg,#fff 0%,#eef4fa 45%,#fff 60%,#e9f1f9 100%);overflow:hidden}
.fourfold .bands{position:absolute;inset:0}
.panel{position:absolute;top:0;width:270px;height:490px;text-align:center}
.panel:nth-of-type(1){left:0}.panel:nth-of-type(2){left:270px}.panel:nth-of-type(3){left:540px}.panel:nth-of-type(4){left:810px}
.panel+.panel{border-left:1px solid rgba(0,0,0,.06)}
.brand{color:var(--blue-mid);font-family:"Poppins",sans-serif;font-weight:600;line-height:1}
.panel .brand{margin-top:30px}
.brand .name{display:block;font-size:24px;letter-spacing:1px}
.brand .sub{display:block;font-size:8px;letter-spacing:1px;margin-top:3px}
.modalities{display:inline-block;font-size:5.5px;color:var(--blue);border-top:1px solid var(--blue-mid);border-bottom:1px solid var(--blue-mid);padding:1px 4px;margin-top:5px;letter-spacing:.5px;font-weight:600}
.location{font-family:"Poppins",sans-serif;font-weight:700;color:var(--blue);font-size:17px;margin-top:8px}
.services{margin:8px auto 0;width:208px;border:1.5px solid var(--blue);border-radius:7px;overflow:hidden;font-size:7.6px;line-height:1.25;text-align:left;background:#fff}
.services .row{display:grid;grid-template-columns:1fr 1fr;padding:2px 6px;border-top:1px solid var(--blue)}
.services .row:first-child{border-top:0}
.services .row:nth-child(even){background:var(--grey-light)}
.services.short{margin-top:22px}
.rule{width:170px;height:1px;background:#444;margin:10px auto 0}
.blurb{font-size:8px;line-height:1.3;margin:7px auto 0;width:190px}
.info{position:absolute;left:0;right:0;top:282px}
.facility{font-size:9px;font-weight:700;color:var(--blue-mid);line-height:1.3}
.address{font-size:7.5px;line-height:1.3}
.address.small{font-size:6px}
.hours-title{margin-top:12px;font-size:10px;font-weight:700;color:var(--blue-mid);line-height:1.3}
.hours{font-size:7.5px;line-height:1.4;width:170px;margin:2px auto 0}
.hours div{display:flex;justify-content:space-between}
.hours span.dots{flex:1;border-bottom:1px dotted #444;margin:0 2px 3px}
.contact{font-size:8.3px;font-weight:700;margin-top:9px;line-height:1.25}
.contact .num{color:var(--blue-mid)}
.contact+.contact{margin-top:6px}
.tagline{position:absolute;left:0;right:0;top:424px;font-family:"Poppins",sans-serif;font-size:17px;line-height:1.2;color:var(--blue-mid);font-weight:300}
.tagline b{font-weight:700}

/* ---------- sheets ---------- */
.sheet{position:absolute;top:565px;width:470px;height:605px;background:linear-gradient(170deg,#fff 0%,#eef4fa 55%,#fff 100%);overflow:hidden}
.sheet-physician{left:105px}
.sheet-patient{left:625px}
.sheet svg.shape{position:absolute;inset:0}
.photo{position:absolute}
.sheet-physician .brand{position:absolute;left:40px;top:32px;text-align:center;width:150px}
.sheet-physician .brand .name{font-size:27px}
.sheet-physician .brand .sub{font-size:9px}
.sheet-physician .modalities{font-size:6px}
.modality-title{position:absolute;left:27px;top:128px;font-family:"Roboto Condensed",sans-serif;font-size:32px;color:#666}
.modality-title span{color:var(--blue)}
.intro{position:absolute;left:28px;top:168px;font-size:11px;font-style:italic;font-weight:600;line-height:1.3}
.intro span{color:var(--blue)}
.question{position:absolute;left:26px;top:236px;font-size:10.5px;font-style:italic;font-weight:600}
.question span{display:block;color:var(--blue)}
.benefits{position:absolute;left:38px;top:278px;width:250px;border:1.5px solid var(--blue);border-radius:8px;overflow:hidden;background:#fff;font-size:11px}
.benefits li{list-style:none;padding:3px 18px;border-top:1px solid var(--blue);color:#333}
.benefits li:first-child{border-top:0}
.benefits li:nth-child(even){background:var(--grey-light)}
.benefits li b{color:var(--blue-mid);font-weight:400}
.body-copy{position:absolute;left:26px;top:366px;width:306px;font-size:7.6px;line-height:1.3;text-align:justify}
.notes{position:absolute;border:1.5px solid var(--blue);border-radius:8px;overflow:hidden;background:#fff;font-size:7.4px;line-height:1.25}
.notes li{list-style:none;padding:3px 12px 3px 26px;border-top:1px solid var(--blue);text-indent:-14px}
.notes li:first-child{border-top:0}
.notes li:nth-child(even){background:var(--grey-light)}
.sheet-physician .notes{left:24px;top:462px;width:304px}

.sheet-patient .badge{position:absolute;left:325px;top:150px;width:148px;height:148px;border-radius:50%;background:var(--blue);border:6px solid #fff;box-shadow:0 0 0 4px #c9c9c9;display:flex;align-items:center;justify-content:center;text-align:center}
.sheet-patient .badge .brand{color:#fff}
.sheet-patient .badge .name{font-size:24px}
.sheet-patient .badge .sub{font-size:8.5px}
.promise{position:absolute;left:34px;top:238px;font-family:"Poppins",sans-serif;font-weight:300;font-size:25px;color:var(--blue-mid);border-bottom:1px solid var(--blue-mid);letter-spacing:.5px;line-height:1.15}
.exam{position:absolute;left:96px;top:274px;font-family:"Poppins",sans-serif;font-weight:700;font-size:28px;color:var(--blue)}
.patient-copy{position:absolute;left:28px;top:314px;width:268px;font-size:7.3px;line-height:1.3;font-style:italic;text-align:justify}
.patient-copy p+p{margin-top:6px}
.sheet-patient .notes{left:18px;top:440px;width:256px}
.footer-band{position:absolute;left:0;right:0;bottom:0;height:16px;background:var(--blue)}
</style>
</head>
<body>

<section class="fourfold">
  <svg class="bands" viewBox="0 0 1080 490" preserveAspectRatio="none" aria-hidden="true">
    <path d="M0 0H1080V40C900 18 780 28 540 26C300 24 150 12 0 14Z" fill="var(--blue)"/>
    <path d="M0 14C150 12 300 24 540 26C780 28 900 18 1080 40V46C900 26 780 34 540 32C300 30 150 20 0 20Z" fill="#9a9a9a"/>
    <path d="M0 470C200 460 400 468 600 460C800 452 950 460 1080 455V490H0Z" fill="var(--blue)"/>
    <path d="M0 462C200 452 400 460 600 452C800 444 950 452 1080 448V455C950 460 800 452 600 460C400 468 200 460 0 470Z" fill="#9a9a9a"/>
  </svg>

  <article class="panel">
    <div class="brand"><span class="name">KEL MRI</span><span class="sub">&amp; IMAGING CENTERS</span></div>
    <div class="modalities">MRI • CT • X-RAY • U/S • DEXA • MAMMO</div>
    <h2 class="location">PALMVIEW</h2>
    <div class="services">
      <div class="row"><span>i) Open MRI/MRA<br>High Field MRI/MRA</span><span>iv) Mammography</span></div>
      <div class="row"><span>ii) Helical CT/CTA</span><span>v) Ultrasound</span></div>
      <div class="row"><span>iii) Digital X-ray</span><span>vi) DXA Bone Density</span></div>
    </div>
    <div class="rule"></div>
    <p class="blurb">24-hour routine turnaround. 4-hour STATS. All Radiologists licensed with subspecialty. All technologists licensed &amp; certified. Most insurance plans accepted. Extremely competitive rates.</p>
    <div class="info">
      <p class="facility">OUR PALMVIEW FACILITY IS LOCATED AT</p>
      <p class="address">1200 West Lantern Blvd, Palmview, FL 30101</p>
      <p class="hours-title">HOURS ARE</p>
      <div class="hours"><div>M-F<span class="dots"></span>7am-7pm</div><div>Saturday<span class="dots"></span>8am-4pm</div></div>
      <p class="contact">Your facility manager can be reached<br><span class="num">at 555-010-2020</span></p>
      <p class="contact">Your marketing liaison can be reached<br><span class="num">at 555-010-3030</span></p>
    </div>
    <p class="tagline"><b>KEL IS</b> KIND EVERY LANE!</p>
  </article>

  <article class="panel">
    <div class="brand"><span class="name">KEL MRI</span><span class="sub">&amp; IMAGING CENTERS</span></div>
    <div class="modalities">MRI • CT • X-RAY • U/S • DEXA • MAMMO</div>
    <h2 class="location">SEABROOK</h2>
    <div class="services">
      <div class="row"><span>i) Open MRI/MRA<br>High Field MRI/MRA</span><span>iv) Mammography</span></div>
      <div class="row"><span>ii) Helical CT/CTA</span><span>v) Ultrasound</span></div>
      <div class="row"><span>iii) Digital X-ray</span><span>vi) DXA Bone Density</span></div>
    </div>
    <div class="rule"></div>
    <p class="blurb">24-hour routine turnaround. 4-hour STATS. All Radiologists licensed with subspecialty. All technologists licensed &amp; certified. Most insurance plans accepted. Extremely competitive rates.</p>
    <div class="info">
      <p class="facility">OUR SEABROOK FACILITY IS LOCATED AT</p>
      <p class="address">4400 N. Harbor Road, Suite 12, Seabrook FL 30102</p>
      <p class="hours-title">HOURS ARE</p>
      <div class="hours"><div>M-F<span class="dots"></span>8am-5pm</div></div>
      <p class="contact">Your facility manager can be reached<br><span class="num">at 555-010-2020</span></p>
      <p class="contact">Your marketing liaison can be reached<br><span class="num">at 555-010-3030</span></p>
    </div>
    <p class="tagline"><b>KEL IS</b> KIND EVERY LANE!</p>
  </article>

  <article class="panel">
    <div class="brand"><span class="name">KEL MRI</span><span class="sub">&amp; IMAGING CENTERS</span></div>
    <div class="modalities">MRI • CT • X-RAY • U/S • DEXA • MAMMO</div>
    <h2 class="location">CEDAR HILL</h2>
    <div class="services">
      <div class="row"><span>i) High-field MRI/MRA</span><span>iv) Mammography</span></div>
      <div class="row"><span>ii) Helical CT/CTA</span><span>v) Color, 3D-4D Ultrasound</span></div>
      <div class="row"><span>iii) Digital X-ray</span><span></span></div>
      <div class="row"><span>iii) DXA/Bone Density</span><span>vi) Breast Biopsy</span></div>
    </div>
    <div class="rule"></div>
    <p class="blurb">24-hour routine turnaround. 4-hour STATS. All Radiologists licensed with subspecialty. All technologists licensed &amp; certified. Most insurance plans accepted. Extremely competitive rates.</p>
    <div class="info">
      <p class="facility">OUR CEDAR HILL FACILITY IS LOCATED AT</p>
      <p class="address">7700 Maple Street Suite 5, Cedar Hill FL 30103</p>
      <p class="hours-title">HOURS ARE</p>
      <div class="hours"><div>M-F<span class="dots"></span>8am-5pm</div></div>
      <p class="contact">Your facility manager can be reached<br><span class="num">at 555-010-2020</span></p>
      <p class="contact">Your marketing liaison can be reached<br><span class="num">at 555-010-3030</span></p>
    </div>
    <p class="tagline"><b>KEL IS</b> KIND EVERY LANE!</p>
  </article>

  <article class="panel">
    <div class="brand"><span class="name">KEL MRI</span><span class="sub">&amp; IMAGING CENTERS</span></div>
    <div class="modalities">MRI • CT • X-RAY • U/S • DEXA • MAMMO</div>
    <h2 class="location">BAY HARBOR</h2>
    <div class="services short">
      <div class="row"><span>i) High-field MRI/MRA</span><span>iv) Mammography</span></div>
      <div class="row"><span>ii) CR X-ray</span><span>v) Color 3D Ultrasound</span></div>
    </div>
    <div class="rule" style="margin-top:24px"></div>
    <p class="blurb">24-hour routine turnaround. 4-hour STATS. All Radiologists licensed with subspecialty. All technologists licensed &amp; certified. Most insurance plans accepted. Extremely competitive rates.</p>
    <div class="info">
      <p class="facility">OUR BAY HARBOR FACILITY IS LOCATED AT</p>
      <p class="address small">950 North Ridge Trail, Suite 8, Bay Harbor FL 30104</p>
      <p class="hours-title">HOURS ARE</p>
      <div class="hours"><div>M-F<span class="dots"></span>8am-5pm</div></div>
      <p class="contact">Your facility manager can be reached<br><span class="num">at 555-010-2020</span></p>
      <p class="contact">Your marketing liaison can be reached<br><span class="num">at 555-010-3030</span></p>
    </div>
    <p class="tagline"><b>KEL IS</b> KIND EVERY LANE!</p>
  </article>
</section>

<section class="sheet sheet-physician">
  <div class="photo" role="img" aria-label="Photo of two radiologists reviewing an X-ray film" style="left:240px;top:6px;width:230px;height:176px;background:linear-gradient(135deg,#f4f7fa 0%,#d7e2ec 50%,#c9d3dc 100%)"></div>
  <svg class="shape" viewBox="0 0 470 605" aria-hidden="true">
    <path d="M0 220C140 212 300 190 470 145V165C330 205 150 226 0 226Z" fill="var(--blue)"/>
    <path d="M470 165C380 205 330 260 330 330C330 430 380 520 470 605V250C440 290 420 330 470 380Z" fill="#a7a7a7" opacity=".55"/>
    <path d="M470 200C400 240 360 290 360 360C360 450 410 540 470 590Z" fill="var(--blue)" opacity=".9"/>
  </svg>
  <div class="photo" role="img" aria-label="Photo of a smiling physician in a white coat with stethoscope" style="left:340px;top:312px;width:125px;height:285px;border-radius:40px 40px 0 0;background:linear-gradient(180deg,#e9eef3 0%,#f8f9fb 60%,#d9e1ea 100%)"></div>
  <div class="brand"><span class="name">KEL MRI</span><span class="sub">&amp; IMAGING CENTERS</span><span class="modalities">MRI • CT • X-RAY • U/S • DEXA • MAMMO</span></div>
  <h1 class="modality-title">DIGITAL <span>X-RAY</span></h1>
  <p class="intro">KEL MRI &amp; Imaging Centers proudly offers<br><span>the latest Digital X-ray.</span></p>
  <p class="question">Why not provide your patients with state-of-the-art diagnostics?<span>Benefits of digital X-ray include:</span></p>
  <ul class="benefits">
    <li><b>i)</b> Faster exam, less wait time</li>
    <li><b>ii)</b> Decreased radiation</li>
    <li><b>iii)</b> Clearer image quality for diagnosis</li>
  </ul>
  <p class="body-copy">A digital revolution has taken place with the advent of digital radiography (DR) systems — active matrix flat panels consisting of a detection layer deposited over an active matrix array (AMA) of thin film transistors. These flat panel devices can instantly display a higher image quality than conventional systems, and have notably improved workflow as more images can be taken and processed in the same amount of time. Most significant, however, is that DR has at least twice (2X) the dose efficiency of CR or traditional film.</p>
  <ul class="notes">
    <li>i) What does that mean for your patients?<br>Less wait times, lower dose, higher quality, better diagnoses.</li>
    <li>ii) Choose KEL. Choose Kind Every Lane. For your Patients, and for you.</li>
    <li>iii) Ask about our new DR systems today.</li>
    <li>iv) X-ray services offered at our Bay Harbor, Palmview and Cedar Hill locations.</li>
    <li>iii) Include locations/addresses/phone numbers on content-footer</li>
  </ul>
</section>

<section class="sheet sheet-patient">
  <div class="photo" role="img" aria-label="Photo of a doctor with a tablet talking with a smiling patient" style="left:0;top:0;width:470px;height:190px;background:linear-gradient(180deg,#f6f8fa 0%,#e3e9ef 70%,#cfd8e0 100%)"></div>
  <svg class="shape" viewBox="0 0 470 605" aria-hidden="true">
    <path d="M0 160C150 170 330 160 470 140V175C330 200 150 215 0 220Z" fill="#a9a9a9"/>
    <path d="M0 168C150 178 330 168 470 148V158C330 176 150 186 0 178Z" fill="var(--blue)"/>
  </svg>
  <div class="photo" role="img" aria-label="Photo of a happy family of a father and three children" style="left:270px;top:330px;width:200px;height:258px;border-radius:80px 0 0 0;background:linear-gradient(160deg,#f3f6f9 0%,#e2d6cb 55%,#d9e3ec 100%)"></div>
  <div class="badge"><div class="brand"><span class="name">KEL MRI</span><span class="sub">&amp; IMAGING CENTERS</span></div></div>
  <h2 class="promise">KIND EVERY LANE</h2>
  <h1 class="exam">X-RAY</h1>
  <div class="patient-copy">
    <p>Having an x-ray is fast, painless and safe. Your doctor has requested that you have this test done to screen for common problems, or to help diagnose a symptom that you have.</p>
    <p>Congratulations! KEL MRI &amp; Imaging Centers has the latest Digital X-Ray systems.</p>
    <p>There is rarely any preparation required for a conventional X-ray, and in fact we accept walk-ins for this exam. You may need to change into a gown or scrubs that we will provide, depending on the exam and what you are wearing. We recommend that you wear loose-fitting clothing without metal zippers, snaps or jewelry.</p>
  </div>
  <ul class="notes">
    <li>i) Most X-rays take less than 10 minutes to perform. To minimize any wait time, please give us a call to schedule an appointment.</li>
    <li>ii) We look forward to getting your X-ray done quickly and results back to your doctor the same or next day.</li>
    <li>iii) We take most health insurance plans, have expert Radiologists &amp; Technologists, state-of-the-art equipment, convenient locations and hours.</li>
    <li>iv) Choose KEL. Choose Kind-Every-Lane. Place locations that offer X-ray in the footer.</li>
  </ul>
  <div class="footer-band"></div>
</section>

</body>
</html>
```